Design for online reviews widget

Attached is a wireframe of a widget we need designing to display reviews on websites from multiple sources. We need this provided at 3 different sizes including full screen, contained (like the wireframe) and mobile.
You have completely free rein on the styling.
The only elements that should remain untouched are the blue stars (https://www.filquarry.net/s/8vtmwp2291zq4h/kv%20stars.ai?dl=0) and powered by logo at the bottom.
Ignore the menu at the top of the wireframe, this is just from the website the widget will be placed on.
Businesses

```html
<!DOCTYPE html>
<html lang="en">
<head>
<meta charset="utf-8">
<title>Reviews widget</title>
<link rel="stylesheet" href="https://fonts.googleapis.com/css2?family=Poppins:wght@400;500;600;700&display=swap">
<style>
:root{
  --accent:#27bdf0;
  --ink:#1c1c1c;
  --body:#4a4a4a;
  --muted:#6b6b6b;
  --rule:#dedede;
  --disc:#f2f2f2;
  --gold:#f6b019;
  --navy:#0d4fa0;
  --white:#ffffff;
}
*{box-sizing:border-box;margin:0;padding:0}
html,body{width:900px;height:1200px;overflow:hidden;background:var(--white)}
body{font-family:"Poppins",sans-serif;color:var(--body);position:relative}
.widget-header{position:absolute;left:67px;top:0;width:766px;height:93px;border-bottom:1px solid var(--rule)}
.score-stars{position:absolute;left:324px;top:19px;display:flex;gap:6px}
.score-stars svg{width:35px;height:35px}
.score-text{position:absolute;left:0;width:766px;top:60px;text-align:center;font-size:12px;color:var(--muted);letter-spacing:.2px}
.filter{position:absolute;right:0;top:31px;width:162px;height:33px;border-radius:17px;background:#f1f1f1;font-size:10px;color:var(--muted);padding:0 20px;display:flex;align-items:center;justify-content:space-between}
.filter svg{width:8px;height:8px}
.review{position:absolute;left:67px;width:766px}
.review.featured{background:var(--white);border-radius:8px;border-bottom:1.5px solid var(--accent);box-shadow:0 8px 28px rgba(0,0,0,.09)}
.source{position:absolute;left:43px;width:110px;height:110px;border-radius:50%;background:var(--disc);display:flex;flex-direction:column;align-items:center;justify-content:center;gap:5px}
.source-name{font-size:11px;font-weight:600;color:var(--ink)}
.rating-stars{display:flex;gap:2px}
.rating-stars svg{width:10px;height:10px}
.score-badge{width:45px;height:45px;border-radius:50%;border:2px solid var(--navy);display:flex;align-items:center;justify-content:center}
.score-badge span{width:37px;height:37px;border-radius:50%;background:var(--navy);color:var(--white);font-size:11px;font-weight:700;display:flex;align-items:center;justify-content:center}
.content{position:absolute;left:170px;width:555px}
.title{font-size:15px;font-weight:700;color:var(--ink);line-height:22px}
.text{margin-top:7px;font-size:11.2px;line-height:16.7px}
.meta{margin-top:11px;font-size:10px;line-height:14px}
.meta b{font-weight:600;color:#444}
.info{margin-top:5px;font-size:9.3px;color:var(--muted);display:flex;gap:10px;align-items:center}
.info span{display:flex;align-items:center;gap:4px}
.info svg{width:9px;height:9px}
.divider{position:absolute;left:240px;top:803px;width:543px;border-top:1px dashed #cfcfcf}
.load-more{position:absolute;left:385px;top:993px;width:130px;height:38px;border-radius:19px;background:var(--accent);color:var(--white);font-size:11.5px;font-weight:700;display:flex;align-items:center;justify-content:center;letter-spacing:.2px}
.footer{position:absolute;left:67px;top:1096px;width:766px;border-top:1px solid var(--rule)}
.powered{position:absolute;left:403px;top:1111px;font-size:16px;color:var(--ink)}
.brand{position:absolute;left:345px;top:1133px;display:flex;align-items:center;gap:8px}
.brand i{width:40px;height:40px;border-radius:50%;background:var(--accent);display:block}
.brand span{font-size:24px;font-weight:700;color:var(--ink)}
</style>
</head>
<body>
<svg width="0" height="0" style="position:absolute">
  <defs>
    <symbol id="star" viewBox="0 0 24 24"><path d="M12 2l2.9 6.3 6.9.7-5.2 4.6 1.5 6.8L12 17l-6.1 3.4 1.5-6.8L2.2 9l6.9-.7z"/></symbol>
    <symbol id="clock" viewBox="0 0 12 12"><circle cx="6" cy="6" r="6" fill="#27bdf0"/><path d="M6 3v3h2.5" stroke="#fff" stroke-width="1.2" fill="none"/></symbol>
    <symbol id="pin" viewBox="0 0 12 12"><path d="M6 .5a4 4 0 0 0-4 4c0 3 4 7 4 7s4-4 4-7a4 4 0 0 0-4-4z" fill="#27bdf0"/><circle cx="6" cy="4.5" r="1.5" fill="#fff"/></symbol>
  </defs>
</svg>

<header class="widget-header">
  <div class="score-stars">
    <svg viewBox="0 0 36 36"><circle cx="18" cy="18" r="18" fill="var(--accent)"/><use href="#star" x="6" y="6" width="24" height="24" fill="#fff"/></svg>
    <svg viewBox="0 0 36 36"><circle cx="18" cy="18" r="18" fill="var(--accent)"/><use href="#star" x="6" y="6" width="24" height="24" fill="#fff"/></svg>
    <svg viewBox="0 0 36 36"><circle cx="18" cy="18" r="18" fill="var(--accent)"/><use href="#star" x="6" y="6" width="24" height="24" fill="#fff"/></svg>
  </div>
  <p class="score-text">Combined Review Score 4.3 out of 5</p>
  <div class="filter">Filter results <svg viewBox="0 0 8 8"><path d="M1 2.5l3 3 3-3" stroke="#333" stroke-width="1.3" fill="none"/></svg></div>
</header>

<article class="review" style="top:174px;height:160px">
  <div class="source" style="top:0">
    <span class="source-name">Fixwise</span>
    <div class="score-badge"><span>9.77</span></div>
  </div>
  <div class="content" style="top:0">
    <h3 class="title">Front door with windows each side and side window</h3>
    <p class="text">This is the second time we have used keystone home Improvments , and the service is amazing! Owen came round several times as we keep changing our minds and he was so helpful and gave us good advice, and the guys who do the fitting are efficient and tidy . I've got to say the end result is amazing and I have recommended to many of friends . Thanks Keystone</p>
    <p class="meta"><b>Reliablity:</b> 9.38 <b>Courtesy:</b> 10 <b>Tidiness:</b> 9.84 <b>Workmanship:</b> 10</p>
    <div class="info"><span><svg><use href="#clock"/></svg>Verified 28th September 2021</span><span><svg><use href="#pin"/></svg>Located in Ashford</span></div>
  </div>
</article>

<article class="review featured" style="top:362px;height:210px">
  <div class="source" style="top:35px;left:43px">
    <span class="source-name">Searchly</span>
    <div class="rating-stars"><svg><use href="#star" fill="var(--gold)"/></svg><svg><use href="#star" fill="var(--gold)"/></svg><svg><use href="#star" fill="var(--gold)"/></svg><svg><use href="#star" fill="var(--gold)"/></svg><svg><use href="#star" fill="var(--gold)"/></svg></div>
  </div>
  <div class="content" style="top:29px;left:169px">
    <h3 class="title">Positive: Professionalism, Quality, Value</h3>
    <p class="text">The team did a good job of replacing a large feature window spanning two floors, as well as the others in my property. They're a professional group who were willing to work out solutions to any problem, especially compared to other companies. Prices are fair, and my new UPVC windows look great. Special thanks to Frank for being so accommodating and for the good communication throughout.</p>
    <p class="meta" style="margin-top:17px"><b>Service:</b> Window installation</p>
    <div class="info"><span><svg><use href="#clock"/></svg>11 months ago by Daniel Hart</span></div>
  </div>
</article>

<article class="review" style="top:620px;height:160px">
  <div class="source" style="top:0">
    <span class="source-name">Localbook</span>
    <div class="rating-stars"><svg><use href="#star" fill="var(--gold)"/></svg><svg><use href="#star" fill="var(--gold)"/></svg><svg><use href="#star" fill="var(--gold)"/></svg><svg><use href="#star" fill="var(--gold)"/></svg><svg><use href="#star" fill="var(--gold)"/></svg></div>
  </div>
  <div class="content" style="top:0">
    <h3 class="title">Brilliant all round professional, friendly service.</h3>
    <p class="text">This home run friendly business was a real pleasure to deal with. From the professional, no pressure quote, nothing was too much trouble to ensure everything is as required for your needs with the quote and fitting. The workmanship and double glazing being fitted was brilliant and my home/outdoors was left tidy and clean leaving an outstanding impression for such an all round professional job. I would not hesitate to recommend this company, such a brilliant service from great hardworking people that care about their service.</p>
    <div class="info" style="margin-top:11px"><span><svg><use href="#clock"/></svg>13 Feb 2018 by GreenChair4</span></div>
  </div>
</article>

<div class="divider"></div>

<article class="review" style="top:837px;height:130px">
  <div class="source" style="top:0">
    <span class="source-name">Verivue</span>
    <div class="rating-stars"><svg><use href="#star" fill="var(--gold)"/></svg><svg><use href="#star" fill="var(--gold)"/></svg><svg><use href="#star" fill="var(--gold)"/></svg><svg><use href="#star" fill="var(--gold)"/></svg><svg><use href="#star" fill="var(--gold)"/></svg></div>
  </div>
  <div class="content" style="top:0">
    <h3 class="title">Front door with windows each side and side window</h3>
    <p class="text">This is the second time we have used keystone home Improvments , and the service is amazing! Owen came round several times as we keep changing our minds and he was so helpful and gave us good advice, and the guys who do the fitting are efficient and tidy . I've got to say the end result is amazing and I have recommended to many of friends . Thanks Keystone</p>
    <div class="info" style="margin-top:11px"><span><svg><use href="#clock"/></svg>13 Feb 2018 by Jo</span></div>
  </div>
</article>

<div class="load-more">LOAD MORE</div>

<footer class="footer"></footer>
<p class="powered">Powered by</p>
<div class="brand"><i></i><span>ScoreGather</span></div>
</body>
</html>
```